The Leadership Horizon Business Card

We need an attractive business card with the logo that we bought from ArtQuarry last year.
Our mission is to contribute to change the way today's leaders manage business companies bringing value to the workplace and helping them to build a new model of creating wealth.
Our logo is clear about our values : we seek Positive Change through People and are convinced that the pursuit of individual well-being and the chase of economic results can converge with the right management.
Industry/Entity Type
Management Consulting
Contact Information for Business Card
Corinne Valbrec
+34 612 80 27 35
corinne.valbrec@leadershiphorizonexample.com
www.leadershiphorizonexample.com
Look and feel
Each slider illustrates characteristics of the customer's brand and the style your logo design should communicate.

```html
<!DOCTYPE html>
<html lang="en">
<head>
<meta charset="utf-8">
<title>The Leadership Horizon – Business Card</title>
<link rel="stylesheet" href="https://fonts.googleapis.com/css2?family=Montserrat:wght@400;500;600&display=swap">
<style>
  :root {
    --page-bg: #2b2b2b;
    --card-white: #ffffff;
    --brand-teal: #0f8580;
    --name-teal: #127f7b;
    --text-grey: #7a7a7a;
    --watermark: #f3f3f3;
  }
  * { margin: 0; padding: 0; box-sizing: border-box; }
  html, body {
    width: 1200px;
    height: 864px;
    overflow: hidden;
    background: var(--page-bg);
    font-family: "Montserrat", Arial, sans-serif;
  }
  .canvas {
    position: relative;
    width: 1200px;
    height: 864px;
  }
  .card {
    position: absolute;
    top: 312px;
    width: 421px;
    height: 240px;
    border-radius: 12px;
    overflow: hidden;
  }
  .card--front {
    left: 174px;
    background: var(--card-white);
  }
  .card--back {
    left: 606px;
    background: var(--brand-teal);
  }
  .front__watermark {
    position: absolute;
    left: 10px;
    top: 30px;
    width: 400px;
    height: 210px;
    border-radius: 50% 50% 0 0;
    background: radial-gradient(ellipse at 50% 45%, var(--watermark) 0%, rgba(243,243,243,0.6) 55%, rgba(255,255,255,0) 80%);
  }
  .front__details {
    position: absolute;
    left: 0;
    top: 0;
    width: 100%;
    text-align: center;
    color: var(--text-grey);
  }
  .contact-name {
    position: absolute;
    top: 71px;
    width: 100%;
    font-size: 16px;
    font-weight: 500;
    color: var(--name-teal);
  }
  .contact-role {
    position: absolute;
    top: 91px;
    width: 100%;
    font-size: 11.5px;
  }
  .contact-rule {
    position: absolute;
    top: 113px;
    left: 193px;
    width: 34px;
    height: 1px;
    background: var(--brand-teal);
  }
  .contact-line {
    position: absolute;
    width: 100%;
    font-size: 11.5px;
    line-height: 1;
  }
  .contact-phone { top: 125px; }
  .contact-email { top: 141px; }
  .contact-web { top: 157px; }
  .brand-lockup {
    position: absolute;
    left: 0;
    top: 0;
    width: 100%;
    height: 100%;
    display: flex;
    flex-direction: column;
    align-items: center;
    justify-content: center;
    gap: 16px;
    padding-bottom: 14px;
  }
  .brand-mark {
    width: 22px;
    height: 22px;
    border-radius: 50%;
    background: var(--card-white);
  }
  .brand-name {
    font-size: 24px;
    font-weight: 600;
    color: var(--card-white);
    letter-spacing: 0.5px;
  }
</style>
</head>
<body>
<main class="canvas">
  <section class="card card--front">
    <div class="front__watermark" role="img" aria-label="Faint brand emblem decoration"></div>
    <div class="front__details">
      <p class="contact-name">Corinne Valbrec</p>
      <p class="contact-role">President</p>
      <div class="contact-rule"></div>
      <p class="contact-line contact-phone">+34 612 80 27 35</p>
      <p class="contact-line contact-email">corinne.valbrec@leadershiphorizonexample.com</p>
      <p class="contact-line contact-web">www.leadershiphorizonexample.com</p>
    </div>
  </section>
  <section class="card card--back">
    <div class="brand-lockup">
      <span class="brand-mark"></span>
      <p class="brand-name">The Leadership Horizon</p>
    </div>
  </section>
</main>
</body>
</html>
```